Harbor Vantage Web Design Project

We need a website design for a start up company called "Harbor Vantage". We provide business consultancy services as well as technology-related services (IT). The design should communicate simplicity and elegance. The domain name of the site will be harborvantage-example.com. The logo of the company is https://files.example-share.net/u/7418205/4630_2116587_67315_image.jpg

Target Market(s)

SMB, Corporates, Semi-governments, Governments.

Industry/Entity Type

Business

Requirements
Must have
• - The background of the pages should be white or soft grey, but we are open for suggestions.
- The pages should have nice menu animations.
- The pages should be "portal-style", with multiple placeholders for different sections and multiple tabs.
Nice to have
• The page should auto-fit the screen and scroll vertically as much as needed.
Should not have
• - Flash Animations.
- Generic Photos.

```html
<!DOCTYPE html>
<html lang="en">
<head>
<meta charset="utf-8">
<title>Harbor Vantage</title>
<link href="https://fonts.googleapis.com/css2?family=Arimo:wght@400;700&display=swap" rel="stylesheet">
<style>
:root{
  --header-bg:#d9d9d9;
  --ink:#333;
  --red:#b10a0f;
  --red-dark:#7e0004;
  --blue:#1e6fb8;
  --blue-dark:#0a4f92;
  --nav-top:#5a5a5a;
  --nav-bottom:#3b3b3b;
  --sky:#5aaadb;
  --band:#c9cdd3;
  --footer-bg:#2e2e2e;
  --footer-text:#8a8a8a;
  --footer-head:#e2e2e2;
  --white:#fff;
}
*{box-sizing:border-box;margin:0;padding:0}
html,body{width:1200px;height:900px;overflow:hidden}
body{font-family:"Arimo",Arial,sans-serif;color:var(--ink);background:var(--white);position:relative}
.abs{position:absolute}

.site-header{left:0;top:0;width:1200px;height:190px;background:var(--header-bg)}
.search{left:876px;top:24px;width:128px;height:29px;background:#454545;border-radius:4px;color:#eee;font-size:18px;padding:4px 0 0 11px}
.search svg{position:absolute;right:8px;top:5px}
.login{left:1011px;top:23px;width:71px;height:31px;background:linear-gradient(#c8141a,var(--red-dark));border-radius:4px;color:#fff;font-size:18px;text-align:center;line-height:31px}
.brand{left:146px;top:96px;display:flex;align-items:center;gap:12px}
.brand-mark{width:40px;height:40px;border-radius:50%;background:var(--blue)}
.brand-name{font-size:34px;font-weight:700;color:var(--blue)}
.tagline{left:519px;top:108px;font-size:24.5px;line-height:32px;color:#3a3a3a}
.tagline .b2b{color:var(--red)} .tagline .b2c{color:var(--blue)}

.main-nav{left:0;top:190px;width:1200px;height:58px;background:linear-gradient(var(--nav-top),var(--nav-bottom));border-top:1px solid #888}
.nav-item{position:absolute;top:0;height:57px;line-height:55px;text-align:center;color:#ddd;font-size:16px;border-left:1px solid #2a2a2a;border-right:1px solid #666}
.nav-item.active{background:linear-gradient(#2a8ee0,#0b5fb0);color:#fff;padding-left:8px}
.nav-item.hover{background:#616161}
.dropdown{left:717px;top:250px;width:214px;height:31px;background:#5b5b5b;color:#ddd;font-size:15px;line-height:31px;padding-left:18px}

.strip-light{left:0;top:248px;width:1200px;height:34px;background:#e9eef0}
.strip-sky{left:0;top:282px;width:1200px;height:24px;background:var(--sky)}
.hero-photo{left:243px;top:282px;width:494px;height:24px;background:linear-gradient(#f0c9b2,#1f1f22)}
.band{left:0;top:306px;width:1200px;height:86px;background:var(--band)}
.band-under{left:0;top:392px;width:1200px;height:20px;background:#eceff2}
.hero-box{left:253px;top:300px;width:473px;height:102px;background:linear-gradient(#c70d12,var(--red-dark));border-radius:0 0 6px 6px;color:#fff;font-size:20px;line-height:24px;text-align:center;padding-top:16px;box-shadow:0 2px 4px rgba(0,0,0,.35)}
.consult{left:787px;top:329px;width:237px;height:58px;border-radius:5px;background:linear-gradient(#2b8ad7,var(--blue-dark));color:#fff;font-size:24px;font-weight:700;line-height:62px;padding-left:11px}
.consult .chev{position:absolute;right:0;top:0;width:54px;height:58px;border-left:2px solid #7fb6e6;display:flex;align-items:center;justify-content:center}

.feature h2{position:absolute;font-size:18px;font-weight:700;color:#222;white-space:nowrap}
.feature p{position:absolute;width:280px;font-size:12px;line-height:18px;color:#444}
.badge{position:absolute;width:139px;height:139px;border-radius:50%;border:1px solid #bbb;background:radial-gradient(circle at 50% 35%,#fff,#d9d9d9);display:flex;align-items:flex-end;justify-content:center;padding-bottom:18px;font-size:24px;font-weight:700;color:var(--red)}
.read-more{position:absolute;width:118px;height:32px;border-radius:4px;background:linear-gradient(#c8141a,var(--red-dark));color:#fff;font-size:18px;text-align:center;line-height:32px}

.site-footer{left:0;top:716px;width:1200px;height:184px;background:var(--footer-bg)}
.site-footer h3{position:absolute;top:21px;font-size:18px;font-weight:400;color:var(--footer-head)}
.foot-list{position:absolute;top:66px;list-style:none;font-size:14px;color:var(--footer-text)}
.foot-list li{height:28px;display:flex;align-items:center}
.dot{width:5px;height:5px;border-radius:50%;background:var(--red);margin-right:24px}
.icon{width:16px;height:16px;margin-right:27px;display:inline-flex;flex-shrink:0}
.post-title{position:absolute;left:343px;top:71px;font-size:15px;font-weight:700;color:#777}
.post-text{position:absolute;left:343px;top:104px;width:210px;font-size:12px;line-height:18px;color:var(--footer-text)}
.contact{position:absolute;left:874px;top:71px;font-size:14px;line-height:18px;color:var(--footer-text)}
.contact .row{display:flex;margin-bottom:22px}
.contact .row.tight{margin-bottom:6px}
.contact .icon{margin-right:18px}
</style>
</head>
<body>

<header class="site-header abs">
  <div class="search abs">Search
    <svg width="16" height="16" viewBox="0 0 16 16"><circle cx="6.5" cy="6.5" r="5" fill="none" stroke="#fff" stroke-width="2"/><line x1="10" y1="10" x2="15" y2="15" stroke="#fff" stroke-width="2.5"/></svg>
  </div>
  <div class="login abs">Log in</div>
  <div class="brand abs"><span class="brand-mark"></span><span class="brand-name">Harbor Vantage</span></div>
  <p class="tagline abs">We develop <span class="b2b">B2B</span> and <span class="b2c">B2C</span> SAAS based solutions &amp;<br>e-commerce portals for companies</p>
</header>

<nav class="main-nav abs">
  <span class="nav-item active" style="left:121px;width:90px">Home</span>
  <span class="nav-item" style="left:211px;width:103px">About Us</span>
  <span class="nav-item" style="left:314px;width:117px">Case Study</span>
  <span class="nav-item" style="left:431px;width:84px">Clients</span>
  <span class="nav-item" style="left:515px;width:68px">Blog</span>
  <span class="nav-item" style="left:583px;width:69px">B2B</span>
  <span class="nav-item" style="left:652px;width:65px">B2C</span>
  <span class="nav-item hover" style="left:717px;width:127px">Our Services</span>
  <span class="nav-item" style="left:844px;width:108px">Marketing</span>
  <span class="nav-item" style="left:952px;width:118px;border-right:none">Contact Us</span>
</nav>

<div class="strip-light abs"></div>
<div class="strip-sky abs"></div>
<div class="hero-photo abs" role="img" aria-label="Photo of a consultant in a dark blouse"></div>
<div class="band abs"></div>
<div class="band-under abs"></div>
<div class="dropdown abs">Marketing Consultant</div>

<div class="hero-box abs">Nam liber tempor cum soluta nobis eleifend<br>option congue nihil imperdiet doming id quod<br>mazim placerat facer possim assum.</div>
<div class="consult abs">Consult NOW!
  <span class="chev"><svg width="30" height="44" viewBox="0 0 30 44"><polyline points="6,4 24,22 6,40" fill="none" stroke="#fff" stroke-width="7"/></svg></span>
</div>

<section class="feature">
  <h2 style="left:293px;top:456px">What is Busines to Busines?</h2>
  <div class="badge" style="left:131px;top:488px" role="img" aria-label="Two business people icon">B2B</div>
  <p style="left:290px;top:496px">When you are marketing to a B2B you want to focus on the logic of the product. You do this by focusing on the features of the product. There is little to no personal emotion involved in the purchasing decision. You want to focus on understanding the organizational buyers and how they operate within the confines of their organization's procedures.</p>
  <span class="read-more" style="left:443px;top:642px">Read more</span>
</section>

<section class="feature">
  <h2 style="left:772px;top:456px">What is Busines to Cunsumer?</h2>
  <div class="badge" style="left:614px;top:488px" role="img" aria-label="Business person and consumer icon">B2C</div>
  <p style="left:770px;top:496px">When you are marketing to a consumer you want to focus on the benefits of the product. Their decision is more emotional. Consumers are different in that they demand a variety of distribution channels for convenience, not so with the B2B market. Consumers are less likely to be interested in a lengthy marketing message.</p>
  <span class="read-more" style="left:938px;top:642px">Read more</span>
</section>

<footer class="site-footer abs">
  <h3 style="left:134px">NAVIGATION</h3>
  <ul class="foot-list" style="left:143px">
    <li><span class="dot"></span>Home</li>
    <li><span class="dot"></span>Information</li>
    <li><span class="dot"></span>About Us</li>
    <li><span class="dot"></span>Blog</li>
  </ul>

  <h3 style="left:341px">LATEST BLOG POST</h3>
  <div class="post-title">Marketing to B2B</div>
  <p class="post-text">When you are marketing to a B2B you want to focus on the logic of the product. You do this by focusing on the features of the product.</p>

  <h3 style="left:618px">FOLLOW US</h3>
  <ul class="foot-list" style="left:632px">
    <li><span class="icon"><svg width="16" height="16"><rect x="1" y="1" width="14" height="14" fill="var(--red)"/></svg></span>Friendbook</li>
    <li><span class="icon"><svg width="16" height="16"><rect x="1" y="1" width="14" height="14" fill="var(--red)"/></svg></span>Chirper</li>
    <li><span class="icon"><svg width="16" height="16"><rect x="1" y="1" width="14" height="14" fill="var(--red)"/></svg></span>Clipstream</li>
    <li><span class="icon"><svg width="16" height="16"><rect x="1" y="3" width="14" height="10" fill="none" stroke="var(--red)" stroke-width="2"/><polyline points="1,3 8,9 15,3" fill="none" stroke="var(--red)" stroke-width="2"/></svg></span>Newsletter</li>
  </ul>

  <h3 style="left:862px">CONTACT INFO</h3>
  <div class="contact">
    <div class="row"><span class="icon"><svg width="16" height="16" viewBox="0 0 16 16"><path d="M8 1a5 5 0 0 1 5 5c0 4-5 9-5 9S3 10 3 6a5 5 0 0 1 5-5z" fill="var(--red)"/><circle cx="8" cy="6" r="2" fill="var(--footer-bg)"/></svg></span><span>Lindgatan 58<br>Norrvik, 4183<br>Nordland</span></div>
    <div class="row tight"><span class="icon"><svg width="16" height="16" viewBox="0 0 16 16"><rect x="3" y="1" width="10" height="14" rx="2" fill="none" stroke="var(--red)" stroke-width="2"/></svg></span><span>+ 999 204 318</span></div>
    <div class="row"><span class="icon"><svg width="16" height="16" viewBox="0 0 16 16"><rect x="3" y="1" width="10" height="14" rx="2" fill="var(--red)"/></svg></span><span>+ 999 204 319</span></div>
  </div>
</footer>

</body>
</html>
```